Picket Sign Advertising For Alaska Tour Company

I would like a relator style picket sign made that I can place by the water near hotels to generate phone calls and website visits. I want to Advertise Our Daily Jet Boat Tours & Jet Ski Tours. This will be a one sided sign. You may be able to see our past brochure and flyer designs and logo. Our FB page is Harlow Summit Excursions and our website is harlowsummitexcursions.com or contact number is 907-418-5563

```html
<!DOCTYPE html>
<html lang="en">
<head>
<meta charset="utf-8">
<title>Daily Jet Boat &amp; Ski Tours – Picket Sign</title>
<link rel="stylesheet" href="https://fonts.googleapis.com/css2?family=Montserrat:wght@700;800;900&display=swap">
<style>
  :root {
    --backdrop: #e9eef1;
    --water-deep: #0f4f6e;
    --water-mid: #1d7fa3;
    --water-light: #5fc0dc;
    --foam: #d9f3fa;
    --ink: #050505;
    --white: #ffffff;
    --gold: #f2c230;
    --logo-gold: #c9a84a;
  }
  * { margin: 0; padding: 0; box-sizing: border-box; }
  html, body {
    width: 1200px; height: 800px; overflow: hidden;
    background: var(--backdrop);
    font-family: "Montserrat", Arial, sans-serif;
  }
  .sign {
    position: absolute; left: 70px; top: 12px;
    width: 1060px; height: 776px;
    overflow: hidden;
    border: 4px solid var(--white);
    box-shadow: 0 6px 20px rgba(0,0,0,.25);
  }
  .water-scene {
    position: absolute; inset: 0;
    background:
      radial-gradient(ellipse 70% 30% at 35% 88%, var(--foam) 0%, rgba(217,243,250,.7) 45%, rgba(217,243,250,0) 75%),
      linear-gradient(175deg, var(--water-deep) 0%, var(--water-mid) 45%, var(--water-light) 78%, var(--foam) 100%);
  }
  .rider-illustration {
    position: absolute; left: 770px; top: 300px;
    width: 290px; height: 355px;
    background: linear-gradient(160deg, #2a8fb0 0%, #8a7a4a 55%, #b79c5a 100%);
    border-radius: 60px 0 0 0;
    opacity: .85;
  }
  .headline {
    position: absolute; left: 70px; top: 60px;
    display: flex; flex-direction: column; align-items: flex-start;
    transform: rotate(-4deg); transform-origin: 0 50%;
    color: var(--white); font-weight: 900;
    text-shadow: 0 4px 8px rgba(0,0,0,.35);
    white-space: nowrap; line-height: .9;
  }
  .headline-daily {
    margin-left: 60px;
    font-size: 50px; color: var(--gold); line-height: 1;
  }
  .headline-row {
    display: flex; align-items: baseline;
  }
  .headline-jet { font-size: 160px; letter-spacing: -3px; }
  .headline-boatski { margin-left: 6px; font-size: 100px; letter-spacing: -2px; }
  .headline-boatski .amp { font-size: 56px; letter-spacing: 0; margin: 0 2px; }
  .headline-tours-row { margin-left: 140px; margin-top: -6px; }
  .headline-tours { font-size: 140px; letter-spacing: -3px; }
  .speed-swoosh { align-self: center; margin-left: 10px; }
  .contact-band {
    position: absolute; left: 0; bottom: 0;
    width: 100%; height: 130px; background: var(--ink);
  }
  .logo-box {
    position: absolute; left: 60px; top: 562px;
    width: 192px; height: 172px; background: var(--ink);
    display: flex; align-items: center; justify-content: center;
    text-align: center; padding: 12px;
  }
  .logo-name {
    color: var(--logo-gold); font-weight: 800;
    font-size: 22px; line-height: 1.2; letter-spacing: 1px;
  }
  .phone-line {
    position: absolute; left: 320px; top: 612px;
    display: flex; align-items: center; gap: 16px;
    color: var(--white); font-weight: 900; font-size: 70px; line-height: 1;
  }
  .website {
    position: absolute; left: 326px; top: 700px;
    color: var(--gold); font-weight: 800; font-size: 30px; letter-spacing: .5px;
  }
</style>
</head>
<body>
  <main class="sign">
    <div class="water-scene" role="img" aria-label="Blue water with white wake and spray"></div>
    <div class="rider-illustration" role="img" aria-label="Illustrated rider on a gold jet ski carving through the water"></div>

    <h1 class="headline">
      <span class="headline-daily">DAILY</span>
      <span class="headline-row">
        <span class="headline-jet">JET</span>
        <span class="headline-boatski">BOAT<span class="amp">&amp;</span>SKI</span>
      </span>
      <span class="headline-row headline-tours-row">
        <span class="headline-tours">TOURS</span>
        <svg class="speed-swoosh" width="200" height="40" viewBox="0 0 200 40" aria-hidden="true">
          <path d="M0 34 L200 2 L8 40 Z" fill="#ffffff"/>
        </svg>
      </span>
    </h1>

    <div class="contact-band"></div>

    <div class="logo-box">
      <span class="logo-name">HARLOW SUMMIT EXCURSIONS</span>
    </div>

    <p class="phone-line">
      <svg width="50" height="50" viewBox="0 0 50 50" aria-hidden="true">
        <circle cx="25" cy="25" r="23" fill="#ffffff"/>
        <path d="M17 13c2-1 3 0 4 2l2 4c1 2 0 3-1 4l-1 1c1 3 3 5 6 6l1-1c1-1 2-2 4-1l4 2c2 1 3 2 2 4-1 3-4 5-7 4-8-2-14-8-16-16-1-3 0-7 2-9z" fill="#050505"/>
      </svg>
      907-418-5563
    </p>
    <p class="website">www.HarlowSummitExcursions.com</p>
  </main>
</body>
</html>
```